Brasko Construction Business Card

I need a business card design for my company.
We are a construction/machinery company.
I would like to see my logo on the front of the card and my details on the other side
I would like the card to be black or dark grey in colour,with my logo as i send it or modified with a lighter blue colour
I would like to see the design kept fairly simple,but eye catching at the same time
Industry/Entity Type
Business
Contact Information for Business Card
Name
Phone Number
Address
Email
Colors
00a990
1b1b1b
000000
474747
ececec

```html
<!DOCTYPE html>
<html lang="en">
<head>
<meta charset="utf-8">
<title>Brasko Construction Business Card</title>
<link rel="stylesheet" href="https://fonts.googleapis.com/css2?family=Open+Sans:wght@400;600;700&display=swap">
<style>
  :root {
    --teal: #00c2ad;
    --teal-deep: #00a990;
    --card: #1b1b1b;
    --grey: #474747;
    --paper: #ececec;
    --white: #ffffff;
  }
  * { box-sizing: border-box; margin: 0; padding: 0; }
  html, body {
    width: 1200px; height: 800px; overflow: hidden;
    background: var(--paper);
    font-family: "Open Sans", Arial, sans-serif;
  }
  .canvas { position: relative; width: 1200px; height: 800px; }

  .card {
    position: absolute;
    background: radial-gradient(circle at 50% 40%, #2b2b2b 0%, var(--card) 75%);
    border-radius: 18px;
    box-shadow: 0 10px 28px rgba(0,0,0,0.25);
    overflow: hidden;
  }

  /* Front */
  .card--front { left: 90px; top: 110px; width: 380px; height: 580px; }
  .front-band {
    position: absolute; left: 52px; top: 0; width: 70px; height: 100%;
    background: var(--teal);
  }
  .front-brand {
    position: absolute; left: 140px; top: 330px; right: 16px;
    display: flex; align-items: center; gap: 12px;
  }
  .front-brand__mark { width: 18px; height: 18px; background: var(--teal); flex: none; }
  .front-brand__name {
    color: var(--white); font-weight: 700; font-size: 20px; line-height: 1.1;
    text-transform: uppercase; letter-spacing: 0.5px; white-space: nowrap;
  }

  /* Back */
  .card--back { left: 530px; top: 210px; width: 590px; height: 350px; }
  .back-brand {
    position: absolute; left: 40px; top: 150px;
    color: var(--white); font-weight: 700; font-size: 22px; line-height: 1.1;
    text-transform: uppercase; letter-spacing: 1px;
  }
  .back-divider {
    position: absolute; left: 280px; top: 60px; width: 2px; height: 230px;
    background: var(--teal-deep);
  }
  .contact { position: absolute; left: 310px; top: 80px; color: var(--white); }
  .contact__name { color: var(--teal); font-weight: 700; font-size: 26px; }
  .contact__title { color: var(--teal); font-weight: 400; font-size: 18px; margin-bottom: 22px; }
  .contact__line {
    display: flex; align-items: center; gap: 8px;
    font-weight: 600; font-size: 16px; line-height: 1.5;
  }
  .contact__icon { width: 14px; height: 14px; fill: var(--teal); flex: none; }
  .contact__address { margin-top: 12px; font-weight: 700; font-size: 16px; line-height: 1.45; }
</style>
</head>
<body>
<main class="canvas">
  <section class="card card--front" aria-label="Card front">
    <div class="front-band"></div>
    <div class="front-brand">
      <span class="front-brand__mark"></span>
      <span class="front-brand__name">Brasko<br>Construction</span>
    </div>
  </section>

  <section class="card card--back" aria-label="Card back">
    <div class="back-brand">Brasko<br>Construction</div>
    <div class="back-divider"></div>
    <div class="contact">
      <p class="contact__name">Daniel R. Hollis</p>
      <p class="contact__title">President</p>
      <p class="contact__line">
        <svg class="contact__icon" viewBox="0 0 24 24" aria-hidden="true"><path d="M6.6 10.8a15.1 15.1 0 0 0 6.6 6.6l2.2-2.2c.3-.3.7-.4 1-.2 1.1.4 2.3.6 3.6.6.6 0 1 .4 1 1V20c0 .6-.4 1-1 1A17 17 0 0 1 3 4c0-.6.4-1 1-1h3.5c.6 0 1 .4 1 1 0 1.3.2 2.5.6 3.6.1.3 0 .7-.2 1z"/></svg>
        (555) 014-2287
      </p>
      <p class="contact__line">
        <svg class="contact__icon" viewBox="0 0 24 24" aria-hidden="true"><path d="M2 5h20v14H2z M2 5l10 8 10-8" fill="var(--teal)" stroke="#1b1b1b" stroke-width="1.5"/></svg>
        dh@braskomail.com
      </p>
      <p class="contact__address">Twelve Harbor Point Road<br>Suite 210<br>Redmond, WA 98052</p>
    </div>
  </section>
</main>
</body>
</html>
```